依頼詳細
演目「ミルフォーネ」。古典バレエの演目で、幼児から大人まで出演いたします。
従来のイメージにこだわりません。添付画像を加工してご使用いただけると幸いです。必ず3人が使用されていることが希望です。かわいいもの、劇画調のもの、クールでシャープなドラマチックな感じのものなど、何でも幅広くお力をお借りできればと思います。
よろしくお願いいたします。
記載項目
主催:ルミエダンス お問合せ先:ルミエダンス事務局 0598-41-6273
サイズ
A4
ページ数
片面
希望イメージ
シンプル 複雑
単色 カラフル
暗い 明るい
日常 高級
遊び心 厳粛
未来的 伝統的
女性的 男性的
希望する色
納品ファイル
• 高解像度JPG (.jpg)
• イラストレーター形式 (.ai)
補足説明
お世話になります。
いろいろなご提案をいただき、ありがとうございます。

ミルフォーネという演目は、イメージがとってもあまり観られる機会もなく、イメージが難しいかと思います。
良い画像ではありませんが、ダンサーを漫画風、劇画調、モノクロ、などに加工していただいたりするものも良いのではないか、という意見も内部でございます。

どうぞお力をお貸しいただけるとうれしいです。
よろしくお願いいたします。
■ 選んだ理由

お世話になっております。
何より鮮やかなレッドのインパクトとバランスの良く大胆な構成に惹かれました。

■ 提案者全員のお礼・コメント

お世話になっております。
この度は多くのご提案をいただき本当にありがとうございました。
どの作品もすばらしく、スタッフ内で票も割れてとても悩みました。
また、機会がございましたらお力を拝借できるとたいへんうれしいです。
ありがとうございました。

```html
<!DOCTYPE html>
<html lang="ja">
<head>
<meta charset="utf-8">
<title>ミルフォーネ 公演ポスター</title>
<link rel="stylesheet" href="https://fonts.googleapis.com/css2?family=Playfair+Display:ital,wght@0,400;1,400&family=Noto+Serif+JP:wght@400;600&display=swap">
<style>
  :root {
    --bg: #f1d2cf;
    --frame: #ffffff;
    --deco-letter: rgba(255,255,255,0.95);
    --ink: #4a302e;
    --ink-soft: #6b4a47;
    --skin: #d9a993;
    --tutu-dark: #2f2326;
    --tutu-pink: #dba6a2;
    --costume-red: #b9554f;
  }
  html, body { margin: 0; padding: 0; overflow: hidden; }
  body { width: 849px; height: 1200px; background: var(--bg); }
  .poster {
    position: relative; width: 849px; height: 1200px; overflow: hidden;
    background: var(--bg);
    font-family: "Noto Serif JP", serif; color: var(--ink);
  }
  .frame { position: absolute; inset: 14px; border: 2px solid var(--frame); }
  .frame-inner { position: absolute; inset: 22px; border: 1px solid var(--frame); }

  .dancer { position: absolute; z-index: 1; }
  .dancer-left { left: 40px; top: 170px; width: 320px; height: 490px; border-radius: 150px 150px 70px 70px;
    background: linear-gradient(180deg, var(--skin), var(--costume-red) 45%, #e9d3cc 75%, #d9b7ae); }
  .dancer-top { left: 490px; top: 34px; width: 280px; height: 420px; border-radius: 130px 130px 90px 90px;
    background: linear-gradient(180deg, var(--skin), #8f6c68 45%, var(--tutu-dark) 80%, #5a4446); }
  .dancer-bottom { left: 345px; top: 540px; width: 455px; height: 625px; border-radius: 200px 200px 90px 90px;
    background: linear-gradient(180deg, var(--skin), var(--tutu-pink) 45%, #c98e8a 100%); }

  .title-letter {
    position: absolute; z-index: 2; font-family: "Playfair Display", serif;
    color: var(--deco-letter); line-height: 1; font-weight: 400;
  }
  .title-letter.large { font-size: 240px; }
  .title-letter.small { font-size: 150px; }

  .show-title { position: absolute; z-index: 3; left: 80px; top: 672px; display: flex; align-items: baseline; gap: 8px; }
  .show-title-latin { font-family: "Playfair Display", serif; font-style: italic; font-size: 52px; color: var(--ink); }
  .show-title-kana { font-size: 14px; color: var(--ink-soft); }

  .performance { position: absolute; z-index: 3; left: 80px; }
  .performance p { margin: 0; }
  .performance-date { font-size: 32px; font-weight: 600; line-height: 1.2; }
  .performance-date small { font-size: 17px; }
  .performance-time { font-size: 12px; margin-top: 2px !important; }
  .performance-venue { font-size: 16px; font-weight: 600; }
  .performance-first { top: 748px; }
  .performance-second { top: 852px; }

  .info { position: absolute; z-index: 3; left: 80px; top: 1060px; font-size: 11px; line-height: 1.7; color: var(--ink); }
  .info p { margin: 0; }
  .seat-badge { display: inline-block; border: 1px solid var(--ink); padding: 0 4px; margin-left: 12px; font-size: 10px; line-height: 1.4; }
  .organizer { position: absolute; z-index: 3; left: 40px; top: 1150px; margin: 0; font-size: 11px; }
</style>
</head>
<body>
<main class="poster">
  <div class="frame"></div>
  <div class="frame-inner"></div>

  <div class="dancer dancer-left" role="img" aria-label="赤いベストと白いスカートの民族衣装で片脚立ちのポーズをとる少女ダンサーの写真"></div>
  <div class="dancer dancer-top" role="img" aria-label="黒いチュチュ姿で両腕を広げる女性ダンサーの写真"></div>
  <div class="dancer dancer-bottom" role="img" aria-label="淡いピンクのチュチュでアラベスクのポーズをとるダンサーの写真"></div>

  <span class="title-letter large" style="left:170px;top:-10px;">Mi</span>
  <span class="title-letter small" style="left:470px;top:250px;">l</span>
  <span class="title-letter small" style="left:500px;top:380px;">f</span>
  <span class="title-letter small" style="left:545px;top:520px;">o</span>
  <span class="title-letter small" style="left:600px;top:660px;">n</span>
  <span class="title-letter small" style="left:655px;top:810px;">e</span>

  <div class="show-title">
    <span class="show-title-latin">Milfone</span>
    <span class="show-title-kana">ミルフォーネ</span>
  </div>

  <section class="performance performance-first">
    <p class="performance-date">3/20<small>(金・祝)</small></p>
    <p class="performance-time">13:00開場 13:30開演</p>
    <p class="performance-venue">水城市民会館 大ホール</p>
  </section>

  <section class="performance performance-second">
    <p class="performance-date">3/28<small>(土)</small>・29<small>(日)</small></p>
    <p class="performance-time">13:00開場 13:30開演</p>
    <p class="performance-venue">緑ヶ丘市民会館 すみれホール</p>
  </section>

  <div class="info">
    <p>【料金】¥1,000(前売り)/¥500<span class="seat-badge">全席自由</span></p>
    <p>【お問合せ】ルミエダンス事務局 0598-41-6273</p>
    <p>http://lumiedance.jp/</p>
  </div>
  <p class="organizer">■主催：ルミエダンス</p>
</main>
</body>
</html>
```